New Zealand Export company needs business cards

We need new business cards to match our new logo for a company based in New Zealand who deal specifically with the Pacific Islands. We source, consolidate and ship products out of New Zealand to the Pacific Islands. Will attach our old ones and also new logo.
Would like the Islands we deal with and the areas of work we have access to, to be included on the business cards.

Contact Information for Business Card

T +64 9 571 3048
F +64 9 571 6285
12-18 Kowhai Lane, Drury, 2113
PO Box 814, Drury, Auckland 2247, New Zealand
www.falconfreight.example.nz
E sales@falconfreight.example.nz

Font styles to use
Sans Serif

Colors
85abd2
33a6d7
ffffff

Requirements
Must have
• A company of PWM

```html
<!DOCTYPE html>
<html lang="en">
<head>
<meta charset="utf-8">
<title>Falcon Freight — Business Cards</title>
<link href="https://fonts.googleapis.com/css2?family=Montserrat:wght@400;500;600;700&display=swap" rel="stylesheet">
<style>
  :root {
    --page-bg: #d0d5d8;
    --card-bg: #ffffff;
    --brand-navy: #1b5aa2;
    --brand-cyan: #33aed2;
    --text-grey: #5a5a5a;
    --title-blue: #2f6fb5;
  }
  * { margin: 0; padding: 0; box-sizing: border-box; }
  html, body {
    width: 1200px; height: 1200px; overflow: hidden;
    background: var(--page-bg);
    font-family: "Montserrat", sans-serif;
  }
  .card {
    position: absolute; left: 259px;
    width: 700px; height: 420px;
    background: var(--card-bg);
  }
  .card--front { top: 122px; }
  .card--back { top: 623px; }

  .wordmark {
    position: absolute;
    color: var(--brand-navy);
    font-weight: 700;
    letter-spacing: 0.02em;
    white-space: nowrap;
    display: flex; align-items: center;
  }
  .wordmark__square {
    display: inline-block;
    background: var(--brand-navy);
    margin-right: 0.35em;
  }
  .card--front .wordmark {
    left: 0; right: 0; top: 180px;
    justify-content: center;
    font-size: 44px;
  }
  .card--front .wordmark__square { width: 34px; height: 34px; }

  .pill {
    position: absolute;
    left: 200px; width: 302px; height: 44px;
    border-radius: 22px;
    display: flex; align-items: center; justify-content: center;
    color: #fff; font-weight: 500; font-size: 21px; letter-spacing: 0.01em;
  }
  .card--front .pill { top: 344px; background: var(--brand-cyan); }
  .card--back .pill { top: 348px; background: var(--brand-navy); }

  .person { position: absolute; left: 80px; top: 68px; }
  .person__name { color: var(--brand-navy); font-weight: 700; font-size: 18.5px; }
  .person__role { color: var(--title-blue); font-size: 14px; margin-top: 6px; }

  .address {
    position: absolute; left: 418px; top: 68px;
    color: var(--text-grey); font-size: 12.5px; line-height: 18.5px;
  }

  .contacts {
    position: absolute; left: 88px; top: 192px;
    list-style: none;
    color: var(--text-grey); font-size: 12.5px;
  }
  .contacts li { display: flex; align-items: center; height: 22px; }
  .contacts__label {
    width: 42px; color: var(--brand-navy);
    font-weight: 600; font-size: 15px;
  }

  .divider {
    position: absolute; left: 335px; top: 200px;
    width: 2px; height: 70px;
    background: var(--brand-navy);
  }
  .card--back .wordmark {
    left: 378px; top: 220px;
    font-size: 22px;
  }
  .card--back .wordmark__square { width: 18px; height: 18px; }
</style>
</head>
<body>
  <section class="card card--front" aria-label="Business card front">
    <div class="wordmark"><span class="wordmark__square"></span>FALCON FREIGHT</div>
    <div class="pill">A COMPANY OF PWM</div>
  </section>

  <section class="card card--back" aria-label="Business card back">
    <div class="person">
      <p class="person__name">TESSA HARLOW</p>
      <p class="person__role">Sales Manager</p>
    </div>
    <address class="address" style="font-style:normal">
      12-18 Kowhai Lane, Drury, 2113<br>
      PO Box 814, Drury, Auckland 2247<br>
      New Zealand
    </address>
    <ul class="contacts">
      <li><span class="contacts__label">T</span>+64 9 571 3048</li>
      <li><span class="contacts__label">F</span>+64 9 571 6285</li>
      <li><span class="contacts__label">E</span>sales@falconfreight.example.nz</li>
      <li><span class="contacts__label">W</span>www.falconfreight.example.nz</li>
    </ul>
    <div class="divider"></div>
    <div class="wordmark"><span class="wordmark__square"></span>FALCON FREIGHT</div>
    <div class="pill">A COMPANY OF PWM</div>
  </section>
</body>
</html>
```